依頼詳細
全国の医科大学の掲示板と、汎療競のHPに掲載されます。医学生が地方の大会を勝ち抜いて汎療競に参加したくなるような、熱く燃えるようなポスターデザインをお待ちしております。
記載項目
第55回汎国療徒競技祭頂点争奪戦
卓球、軟式テニス、バドミントン、バレーボール、バスケットボール、サッカー、弓道、柔道
http://www.hanryokyo.kumoyado.example/top.htmと添付ファイルのQRコード
主管:北杜薬科大学 主催:北陽療徒競技協会、南陽療徒競技協会
サイズ
A2
ページ数
片面
希望イメージ
シンプル 複雑
単色 カラフル
暗い 明るい
日常 高級
遊び心 厳粛
未来的 伝統的
女性的 男性的
希望する色
赤系、黄・オレンジ系、無彩色系、青も欲しいです。
納品ファイル
• 高解像度JPG (.jpg)
• PNG形式 (.png)
補足説明
なるべく1月末までに仕上げて下さると嬉しいです。
■ 選んだ理由

色彩が大変気に入りました。また、王座決定戦の字がとても気に入りました。

■ 提案者全員のお礼・コメント

沢山素敵なポスターを提案してくださり、ありがとうございます。

```html
<!DOCTYPE html>
<html lang="ja">
<head>
<meta charset="utf-8">
<title>第55回汎国療徒競技祭 頂点争奪戦</title>
<link rel="stylesheet" href="https://fonts.googleapis.com/css2?family=Noto+Sans+JP:wght@500;700;900&family=Shippori+Mincho+B1:wght@800&display=swap">
<style>
  :root {
    --ink: #050403;
    --white: #ffffff;
    --red: #e0141e;
    --gold-light: #fff3c4;
    --gold-mid: #e2b25a;
    --gold-deep: #8a5a1c;
    --fur-light: #b07a3e;
    --fur-dark: #3a2410;
    --footer: #d9d9d9;
  }
  html, body { margin: 0; padding: 0; overflow: hidden; background: var(--ink); }
  .poster {
    position: relative;
    width: 849px;
    height: 1200px;
    overflow: hidden;
    background: radial-gradient(ellipse at 50% 30%, #1a1408 0%, var(--ink) 70%);
    font-family: "Noto Sans JP", sans-serif;
    color: var(--white);
  }
  .hero-photo {
    position: absolute;
    left: 90px;
    top: 560px;
    width: 670px;
    height: 640px;
    background:
      radial-gradient(ellipse 45% 40% at 50% 55%, var(--fur-light) 0%, #7a4e22 45%, var(--fur-dark) 75%, transparent 100%);
  }
  .edition {
    position: absolute;
    top: 30px;
    left: 0; right: 0;
    text-align: center;
    font-weight: 700;
    font-size: 40px;
    letter-spacing: 2px;
  }
  .edition .num { font-size: 52px; }
  .event-name {
    position: absolute;
    top: 100px;
    left: 0; right: 0;
    text-align: center;
    font-weight: 900;
    font-size: 62px;
    letter-spacing: 6px;
  }
  .headline {
    position: absolute;
    left: 0; right: 0;
    text-align: center;
    font-family: "Shippori Mincho B1", serif;
    font-weight: 800;
    background: linear-gradient(180deg, var(--gold-light) 0%, var(--gold-mid) 40%, var(--gold-deep) 75%, var(--gold-mid) 100%);
    -webkit-background-clip: text;
    background-clip: text;
    color: transparent;
    line-height: 1;
  }
  .headline.top { top: 195px; font-size: 270px; letter-spacing: 4px; }
  .headline.bottom { top: 460px; font-size: 175px; letter-spacing: 6px; }
  .sports {
    position: absolute;
    top: 210px;
    margin: 0;
    padding: 0;
    list-style: none;
    writing-mode: vertical-rl;
    color: var(--red);
    font-weight: 700;
    font-size: 30px;
    line-height: 1;
  }
  .sports li { margin-bottom: 28px; }
  .sports li::before {
    content: "";
    display: inline-block;
    width: 14px; height: 14px;
    border-radius: 50%;
    background: var(--red);
    margin-bottom: 10px;
  }
  .sports.left { left: 46px; }
  .sports.right { right: 46px; }
  .credits {
    position: absolute;
    left: 250px;
    top: 1100px;
    font-size: 15px;
    line-height: 1.6;
    color: var(--footer);
    font-weight: 500;
  }
</style>
</head>
<body>
  <main class="poster">
    <div class="hero-photo" role="img" aria-label="夜空を見上げる雄ライオンの写真"></div>

    <p class="edition" style="margin:0">第<span class="num">55</span>回</p>
    <h1 class="event-name" style="margin:0">汎国療徒競技祭</h1>
    <div class="headline top">頂点</div>
    <div class="headline bottom">争奪戦</div>

    <ul class="sports left">
      <li>バスケットボール</li>
      <li>サッカー</li>
      <li>弓道</li>
      <li>柔道</li>
    </ul>
    <ul class="sports right">
      <li>卓球</li>
      <li>軟式テニス</li>
      <li>バドミントン</li>
      <li>バレーボール</li>
    </ul>

    <footer class="credits">
      主管：北杜薬科大学<br>
      主催：北陽療徒競技協会、南陽療徒競技協会<br>
      http://www.hanryokyo.kumoyado.example/top.htm
    </footer>
  </main>
</body>
</html>
```